Tavrento - Staffing APP for the hospitality industry.

I need 7 screens designed that form the core of the APP. Tavrento is a staffing APP for the hospitality industry where workers sign up and complete details about themselves and their qualifications and experience. They also switch a button ON and OFF showing their availability status. Venues/employers then scan for workers based on job type, availability, distance etc

Industry/Entity Type

Hospitality employment industry

Number of Pages Required

5+ page

Requirements
Must have
• Refer wire frames supplied
Nice to have
• Here is my website as a guide www.tavrento.com.au
Should not have
• Nil

```html
<!DOCTYPE html>
<html lang="en">
<head>
<meta charset="utf-8">
<title>Tavrento – App Screens</title>
<link href="https://fonts.googleapis.com/css2?family=Nunito+Sans:ital,wght@0,400;0,600;0,700;0,800;1,400;1,600&display=swap" rel="stylesheet">
<style>
:root{
  --bg:#d9dee8;
  --card:#f3f4f8;
  --field:#ffffff;
  --ink:#1f1f22;
  --navy:#1d1b3a;
  --muted:#8a8f9c;
  --soft:#b9bdc7;
  --title:#5d6170;
  --pill:#6f737c;
  --green:#7fd39a;
  --line:#6b7080;
}
*{box-sizing:border-box;margin:0;padding:0}
html,body{width:1002px;height:1200px;overflow:hidden}
body{background:var(--bg);font-family:"Nunito Sans",sans-serif;color:var(--ink);position:relative}
.abs{position:absolute}
.connectors{position:absolute;left:0;top:0}
.brand{position:absolute;left:0;width:276px;top:86px;text-align:center;font-size:22px;font-weight:800;color:var(--ink);letter-spacing:.3px}
.brand .dot{display:inline-block;width:9px;height:9px;background:var(--ink);margin-right:6px;vertical-align:middle}
.update-date{position:absolute;left:0;width:284px;top:145px;text-align:center;font-size:9.7px;font-weight:700;color:var(--title)}
.checklist{position:absolute;left:51px;top:177px;list-style:none;width:200px}
.checklist li{position:relative;padding-left:22px;font-size:9.7px;color:var(--title);line-height:11.5px;margin-bottom:4.3px}
.checklist svg{position:absolute;left:0;top:1px}
.legend{position:absolute;left:38px;top:309px;width:209px;height:93px;background:#fff;border-radius:5px;padding:11px 0 0 16px}
.legend div{position:relative;font-size:7px;color:#6d7180;height:19px;padding-left:20px;line-height:10px}
.legend svg{position:absolute;left:0;top:1px}
.regards{position:absolute;left:0;width:266px;top:471px;text-align:center;font-size:9.5px;color:var(--title)}
.board-title{position:absolute;width:203px;text-align:center;font-size:12.6px;font-weight:600;color:var(--title)}
.board-sub{position:absolute;width:203px;text-align:center;font-size:9.5px;font-style:italic;font-weight:600;color:#8d93a1}
.screen{position:absolute;width:203px;background:var(--card);border-radius:13px;overflow:hidden}
.screen > *{position:absolute}
.clock{left:12px;top:6px;font-size:8.6px;font-weight:600}
.status{right:8px;top:8px}
.icon-btn{width:23px;height:23px;background:#fff;border-radius:6px;display:flex;align-items:center;justify-content:center}
.screen-title{left:0;width:100%;text-align:center;top:35px;font-size:9.5px;font-weight:700;color:var(--navy)}
.role-pill{left:71px;top:63px;width:62px;height:14px;border-radius:4px;background:var(--pill);color:#fff;font-size:7px;font-weight:700;text-align:center;line-height:14px}
.seen{left:0;width:100%;text-align:center;top:84px;font-size:7px;color:var(--soft)}
.photo-back{background:linear-gradient(180deg,#c5c9d2,#dfe2e8);border-radius:7px;top:114px;width:23px;height:134px}
.photo{border-radius:7px;background:linear-gradient(160deg,#4b4a4c 0%,#2a2c31 45%,#6b5a4a 80%,#c9c1b4 100%)}
.worker-name{left:0;width:100%;text-align:center;top:263px;font-size:10.5px;font-weight:700}
.stats-pill{left:64px;top:280px;width:76px;height:18px;background:#fff;border-radius:5px;font-size:8px;font-weight:700;display:flex;align-items:center;justify-content:center;gap:5px}
.stats-pill small{font-weight:400;color:var(--soft);font-size:7px}
.stats-pill i{width:1px;height:11px;background:#d5d8df}
.spec{font-size:7px;top:0}
.spec.k{color:var(--soft)}
.spec.v{font-weight:700}
.chip{top:346px;height:21px;background:#fff;border-radius:5px;font-size:7px;font-weight:700;display:flex;align-items:center;justify-content:space-between;padding:0 7px 0 4px}
.btn-dark{background:var(--ink);color:#fff;border-radius:5px;font-weight:700;display:flex;align-items:center;justify-content:center}
.label{font-size:7px;color:var(--muted);font-weight:600}
.field{background:var(--field);border-radius:5px;font-size:8.5px;display:flex;align-items:center;padding:0 8px}
.field.ph{font-size:7px;color:var(--soft);font-style:italic}
.caret{display:inline-block;width:1px;height:10px;background:var(--ink);margin-left:2px}
.toggle{width:28px;height:15px;border-radius:8px;background:#eceef2}
.toggle::after{content:"";position:absolute;left:2px;top:2px;width:11px;height:11px;border-radius:50%;background:#fff;box-shadow:0 1px 2px rgba(0,0,0,.2)}
.toggle.on{background:var(--green)}
.toggle.on::after{left:15px}
.yn{width:46px;height:20px;background:#fff;border-radius:5px;font-size:7.5px;font-weight:700;display:flex;align-items:center;justify-content:space-around;color:var(--ink)}
.yn span:last-child{color:var(--soft)}
.yn i{width:1px;height:9px;background:#ccc}
.words{font-size:5px;color:var(--soft);font-style:italic}
.hero-photo{left:0;top:0;width:203px;height:270px;background:linear-gradient(180deg,#4a4b4f 0%,#3a3b40 55%,#55565b 100%)}
.hero-name{left:0;width:100%;top:151px;text-align:center;color:#fff;font-size:14px;font-weight:600;letter-spacing:2.5px}
.hero-panel{left:-20px;top:252px;width:243px;height:200px;background:#fff;border-radius:50% 50% 0 0 / 18px 18px 0 0}
</style>
</head>
<body>

<svg class="connectors" width="1002" height="1200" aria-hidden="true">
  <g fill="none" stroke="var(--line)" stroke-width=".8">
    <path d="M246 326H279"/>
    <path d="M246 345H283V365H297"/>
    <path d="M482 326H501V365H536"/>
  </g>
</svg>

<div class="brand"><span class="dot"></span>Tavrento</div>
<div class="update-date">Updates 24 Oct 2022</div>
<ul class="checklist">
  <li><svg width="11" height="11" viewBox="0 0 11 11"><rect x=".5" y=".5" width="10" height="10" rx="2.5" fill="none" stroke="#5d6170"/><path d="M3 5.6l1.7 1.6L8 3.8" fill="none" stroke="#5d6170"/></svg>Screen 2. Legal + Help Updated</li>
  <li><svg width="11" height="11" viewBox="0 0 11 11"><rect x=".5" y=".5" width="10" height="10" rx="2.5" fill="none" stroke="#5d6170"/><path d="M3 5.6l1.7 1.6L8 3.8" fill="none" stroke="#5d6170"/></svg>Screen 3. All Qualification change to Qualifications</li>
  <li><svg width="11" height="11" viewBox="0 0 11 11"><rect x=".5" y=".5" width="10" height="10" rx="2.5" fill="none" stroke="#5d6170"/><path d="M3 5.6l1.7 1.6L8 3.8" fill="none" stroke="#5d6170"/></svg>Screen 4. “TICK and a HEART” Added</li>
  <li><svg width="11" height="11" viewBox="0 0 11 11"><rect x=".5" y=".5" width="10" height="10" rx="2.5" fill="none" stroke="#5d6170"/><path d="M3 5.6l1.7 1.6L8 3.8" fill="none" stroke="#5d6170"/></svg>Screen 4. Back arrow Button Added</li>
</ul>

<div class="legend">
  <div><svg width="8" height="9" viewBox="0 0 8 9"><rect y="1" width="8" height="8" rx="1.5" fill="#6b6f7a"/><rect x="2" width="4" height="2" rx=".6" fill="#6b6f7a"/></svg>Dark Grey Indicate the worker is Eligible</div>
  <div><svg width="8" height="9" viewBox="0 0 8 9"><rect y="1" width="8" height="8" rx="1.5" fill="#c9ccd4"/><rect x="2" width="4" height="2" rx=".6" fill="#c9ccd4"/></svg>Light Grey Indicate the worker is Not Eligible</div>
  <div><svg width="9" height="8" viewBox="0 0 9 8"><path d="M4.5 8L.8 4.3A2.2 2.2 0 014.5 1.3 2.2 2.2 0 018.2 4.3z" fill="#6b6f7a"/></svg>Bold Heart Indicate the worker is Online</div>
  <div><svg width="9" height="8" viewBox="0 0 9 8"><path d="M4.5 8L.8 4.3A2.2 2.2 0 014.5 1.3 2.2 2.2 0 018.2 4.3z" fill="#cdd0d7"/></svg>Fade Heart Indicate the worker is Away</div>
</div>

<div class="regards">Best Regards,</div>

<!-- Board titles -->
<div class="board-title" style="left:277px;top:51px">Scan Results</div>
<div class="board-sub" style="left:277px;top:70px">Updated</div>
<div class="board-title" style="left:522px;top:51px">Favourites</div>
<div class="board-sub" style="left:522px;top:70px">Updated</div>
<div class="board-title" style="left:770px;top:51px">Worker Registration</div>
<div class="board-sub" style="left:770px;top:70px">Updated</div>
<div class="board-title" style="left:34px;top:596px">Front Page</div>
<div class="board-title" style="left:277px;top:596px">Scan Worker</div>
<div class="board-title" style="left:522px;top:596px">Employer Home</div>
<div class="board-sub" style="left:522px;top:615px">Updated</div>

<!-- Scan Results -->
<section class="screen" style="left:279px;top:95px;height:440px">
  <div class="clock">9:41</div>
  <svg class="status" width="34" height="6" viewBox="0 0 34 6"><rect x="0" y="4" width="1.5" height="2" fill="#1f1f22"/><rect x="2.5" y="3" width="1.5" height="3" fill="#1f1f22"/><rect x="5" y="1.5" width="1.5" height="4.5" fill="#1f1f22"/><rect x="7.5" y="0" width="1.5" height="6" fill="#1f1f22"/><path d="M12 2.2a4.5 4.5 0 016 0M13.3 3.6a2.6 2.6 0 013.4 0" fill="none" stroke="#1f1f22" stroke-width="1"/><circle cx="15" cy="5.2" r=".8" fill="#1f1f22"/><rect x="22" y=".5" width="10" height="5" rx="1" fill="#1d1b3a"/><rect x="32.5" y="2" width="1" height="2" fill="#1d1b3a"/></svg>
  <div class="icon-btn" style="left:10px;top:31px"><svg width="6" height="9" viewBox="0 0 6 9"><path d="M5 1L1.5 4.5 5 8" fill="none" stroke="#1f1f22" stroke-width="1.4"/></svg></div>
  <div class="screen-title">Scan Results</div>
  <div class="icon-btn" style="left:170px;top:31px"><svg width="8" height="8" viewBox="0 0 8 8"><path d="M1 1l6 6M7 1L1 7" stroke="#1f1f22" stroke-width="1.4"/></svg></div>
  <div class="role-pill">Chef</div>
  <div class="seen">Last seen 2hr ago</div>
  <div class="photo-back" style="left:11px"></div>
  <div class="photo-back" style="left:169px"></div>
  <div class="photo" role="img" aria-label="Photo of a chef plating a dish in a kitchen" style="left:34px;top:98px;width:135px;height:156px"></div>
  <svg style="left:19px;top:265px" width="8" height="9" viewBox="0 0 8 9"><rect y="1" width="8" height="8" rx="1.5" fill="#c9ccd4"/><rect x="2" width="4" height="2" rx=".6" fill="#c9ccd4"/></svg>
  <div class="worker-name">Marco</div>
  <svg style="left:174px;top:266px" width="9" height="8" viewBox="0 0 9 8"><path d="M4.5 8L.8 4.3A2.2 2.2 0 014.5 1.3 2.2 2.2 0 018.2 4.3z" fill="#cdd0d7"/></svg>
  <div class="stats-pill">28 <small>yr</small><i></i>15 <small>km</small></div>
  <div class="spec k" style="left:15px;top:308px">RSA</div>
  <div class="spec v" style="left:74px;top:308px">Yes</div>
  <div class="spec k" style="left:115px;top:308px">SFH</div>
  <div class="spec v" style="left:174px;top:308px">Yes</div>
  <div class="spec k" style="left:15px;top:323px">Vax Status</div>
  <div class="spec v" style="left:78px;top:323px">F</div>
  <div class="spec k" style="left:115px;top:323px">ABN</div>
  <div class="spec v" style="left:175px;top:323px">No</div>
  <div class="chip" style="left:12px;width:84px">Qualifications<svg width="10" height="10" viewBox="0 0 10 10"><rect x=".5" y=".5" width="9" height="9" rx="3" fill="none" stroke="#1f1f22" stroke-width=".8"/><path d="M4 3l2 2-2 2" fill="none" stroke="#1f1f22" stroke-width=".8"/></svg></div>
  <div class="chip" style="left:107px;width:83px">Experience<svg width="10" height="10" viewBox="0 0 10 10"><rect x=".5" y=".5" width="9" height="9" rx="3" fill="none" stroke="#1f1f22" stroke-width=".8"/><path d="M4 3l2 2-2 2" fill="none" stroke="#1f1f22" stroke-width=".8"/></svg></div>
  <div class="btn-dark" style="left:12px;top:384px;width:110px;height:27px;font-size:9.5px"><svg style="position:absolute;left:10px" width="10" height="10" viewBox="0 0 10 10"><path d="M2 1l2 2-1 1.2a6 6 0 002.8 2.8L7 6l2 2-1.3 1.3C4.5 9.3.7 5.5.7 2.3z" fill="none" stroke="#fff" stroke-width=".9"/></svg>Reveal</div>
  <div class="icon-btn" style="left:131px;top:386px"><svg width="10" height="10" viewBox="0 0 10 10"><rect x=".5" y=".5" width="9" height="9" rx="2" fill="none" stroke="#1f1f22"/><path d="M3.5 2.5v5M7 3L5 5l2 2" fill="none" stroke="#1f1f22"/></svg></div>
  <div class="icon-btn" style="left:165px;top:386px"><svg width="10" height="10" viewBox="0 0 10 10"><rect x=".5" y=".5" width="9" height="9" rx="2" fill="none" stroke="#1f1f22"/><path d="M6.5 2.5v5M3 3l2 2-2 2" fill="none" stroke="#1f1f22"/></svg></div>
</section>

<!-- Favourites -->
<section class="screen" style="left:524px;top:95px;height:440px">
  <div class="clock">9:41</div>
  <svg class="status" width="34" height="6" viewBox="0 0 34 6"><rect x="0" y="4" width="1.5" height="2" fill="#1f1f22"/><rect x="2.5" y="3" width="1.5" height="3" fill="#1f1f22"/><rect x="5" y="1.5" width="1.5" height="4.5" fill="#1f1f22"/><rect x="7.5" y="0" width="1.5" height="6" fill="#1f1f22"/><path d="M12 2.2a4.5 4.5 0 016 0M13.3 3.6a2.6 2.6 0 013.4 0" fill="none" stroke="#1f1f22" stroke-width="1"/><circle cx="15" cy="5.2" r=".8" fill="#1f1f22"/><rect x="22" y=".5" width="10" height="5" rx="1" fill="#1d1b3a"/><rect x="32.5" y="2" width="1" height="2" fill="#1d1b3a"/></svg>
  <div class="icon-btn" style="left:10px;top:31px"><svg width="6" height="9" viewBox="0 0 6 9"><path d="M5 1L1.5 4.5 5 8" fill="none" stroke="#1f1f22" stroke-width="1.4"/></svg></div>
  <div class="screen-title">Favourites</div>
  <div class="icon-btn" style="left:170px;top:31px"><svg width="8" height="8" viewBox="0 0 8 8"><path d="M1 1l6 6M7 1L1 7" stroke="#1f1f22" stroke-width="1.4"/></svg></div>
  <div class="role-pill">Chef</div>
  <div class="seen">Last seen 2hr ago</div>
  <div class="photo-back" style="left:11px"></div>
  <div class="photo-back" style="left:169px"></div>
  <div class="photo" role="img" aria-label="Photo of a chef plating a dish in a kitchen" style="left:34px;top:98px;width:135px;height:156px"></div>
  <svg style="left:19px;top:265px" width="8" height="9" viewBox="0 0 8 9"><rect y="1" width="8" height="8" rx="1.5" fill="#6b6f7a"/><rect x="2" width="4" height="2" rx=".6" fill="#6b6f7a"/></svg>
  <div class="worker-name">Marco</div>
  <svg style="left:174px;top:266px" width="9" height="8" viewBox="0 0 9 8"><path d="M4.5 8L.8 4.3A2.2 2.2 0 014.5 1.3 2.2 2.2 0 018.2 4.3z" fill="#6b6f7a"/></svg>
  <div class="stats-pill">28 <small>yr</small><i></i>15 <small>km</small></div>
  <div class="spec k" style="left:15px;top:308px">RSA</div>
  <div class="spec v" style="left:74px;top:308px">Yes</div>
  <div class="spec k" style="left:115px;top:308px">SFH</div>
  <div class="spec v" style="left:174px;top:308px">Yes</div>
  <div class="spec k" style="left:15px;top:323px">Vax Status</div>
  <div class="spec v" style="left:78px;top:323px">F</div>
  <div class="spec k" style="left:115px;top:323px">ABN</div>
  <div class="spec v" style="left:175px;top:323px">No</div>
  <div class="chip" style="left:12px;width:84px">Qualifications<svg width="10" height="10" viewBox="0 0 10 10"><rect x=".5" y=".5" width="9" height="9" rx="3" fill="none" stroke="#1f1f22" stroke-width=".8"/><path d="M4 3l2 2-2 2" fill="none" stroke="#1f1f22" stroke-width=".8"/></svg></div>
  <div class="chip" style="left:107px;width:83px">Experience<svg width="10" height="10" viewBox="0 0 10 10"><rect x=".5" y=".5" width="9" height="9" rx="3" fill="none" stroke="#1f1f22" stroke-width=".8"/><path d="M4 3l2 2-2 2" fill="none" stroke="#1f1f22" stroke-width=".8"/></svg></div>
  <div class="btn-dark" style="left:12px;top:384px;width:110px;height:27px;font-size:9.5px"><svg style="position:absolute;left:10px" width="10" height="10" viewBox="0 0 10 10"><path d="M2 1l2 2-1 1.2a6 6 0 002.8 2.8L7 6l2 2-1.3 1.3C4.5 9.3.7 5.5.7 2.3z" fill="none" stroke="#fff" stroke-width=".9"/></svg>Reveal</div>
  <div class="icon-btn" style="left:131px;top:386px"><svg width="10" height="10" viewBox="0 0 10 10"><rect x=".5" y=".5" width="9" height="9" rx="2" fill="none" stroke="#1f1f22"/><path d="M3.5 2.5v5M7 3L5 5l2 2" fill="none" stroke="#1f1f22"/></svg></div>
  <div class="icon-btn" style="left:165px;top:386px"><svg width="10" height="10" viewBox="0 0 10 10"><rect x=".5" y=".5" width="9" height="9" rx="2" fill="none" stroke="#1f1f22"/><path d="M6.5 2.5v5M3 3l2 2-2 2" fill="none" stroke="#1f1f22"/></svg></div>
</section>

<!-- Worker Registration -->
<section class="screen" style="left:768px;top:95px;height:834px">
  <div class="clock">9:41</div>
  <svg class="status" width="34" height="6" viewBox="0 0 34 6"><rect x="0" y="4" width="1.5" height="2" fill="#1f1f22"/><rect x="2.5" y="3" width="1.5" height="3" fill="#1f1f22"/><rect x="5" y="1.5" width="1.5" height="4.5" fill="#1f1f22"/><rect x="7.5" y="0" width="1.5" height="6" fill="#1f1f22"/><path d="M12 2.2a4.5 4.5 0 016 0M13.3 3.6a2.6 2.6 0 013.4 0" fill="none" stroke="#1f1f22" stroke-width="1"/><circle cx="15" cy="5.2" r=".8" fill="#1f1f22"/><rect x="22" y=".5" width="10" height="5" rx="1" fill="#1d1b3a"/><rect x="32.5" y="2" width="1" height="2" fill="#1d1b3a"/></svg>
  <div class="icon-btn" style="left:10px;top:31px"><svg width="6" height="9" viewBox="0 0 6 9"><path d="M5 1L1.5 4.5 5 8" fill="none" stroke="#1f1f22" stroke-width="1.4"/></svg></div>
  <div class="screen-title">Worker Registration</div>
  <div class="icon-btn" style="left:170px;top:31px"><svg width="8" height="8" viewBox="0 0 8 8"><path d="M1 1l6 6M7 1L1 7" stroke="#1f1f22" stroke-width="1.4"/></svg></div>
  <div class="photo" role="img" aria-label="Profile photo of a chef at work" style="left:63px;top:62px;width:78px;height:93px"></div>
  <svg style="left:96px;top:102px" width="12" height="12" viewBox="0 0 12 12"><rect x=".5" y=".5" width="11" height="11" rx="3" fill="rgba(255,255,255,.35)" stroke="#fff" stroke-width=".8"/><path d="M3 8l2-2 1.5 1.5L9 5" fill="none" stroke="#fff" stroke-width=".8"/></svg>
  <div class="label" style="left:10px;top:171px">First Name</div>
  <div class="field" style="left:10px;top:186px;width:183px;height:25px">Dylan<span class="caret"></span></div>
  <div class="label" style="left:10px;top:220px">Email Address</div>
  <div class="field" style="left:10px;top:236px;width:183px;height:25px"></div>
  <div class="label" style="left:10px;top:270px">Mobile Phone</div>
  <div class="field" style="left:10px;top:286px;width:183px;height:25px"></div>
  <div class="label" style="left:10px;top:320px">Location</div>
  <div class="field ph" style="left:10px;top:336px;width:66px;height:25px">Street Number</div>
  <div class="field ph" style="left:82px;top:336px;width:111px;height:25px">Street Name</div>
  <div class="field ph" style="left:10px;top:365px;width:183px;height:25px">Suburb / City</div>
  <div class="field ph" style="left:10px;top:394px;width:110px;height:25px">State</div>
  <div class="field ph" style="left:126px;top:394px;width:67px;height:25px">Post Code</div>
  <div class="label" style="left:14px;top:435px">D.O.B</div>
  <div class="field" style="left:47px;top:429px;width:146px;height:20px;justify-content:flex-end"><svg width="9" height="9" viewBox="0 0 9 9"><rect x=".5" y="1.5" width="8" height="7" rx="1.5" fill="none" stroke="#1f1f22" stroke-width=".8"/><path d="M.5 3.5h8M2.5 0v2M6.5 0v2" stroke="#1f1f22" stroke-width=".8"/></svg></div>
  <div class="label" style="left:14px;top:464px">RSA</div>
  <div class="toggle" style="left:62px;top:460px"></div>
  <div class="label" style="left:116px;top:464px">SFA</div>
  <div class="toggle on" style="left:163px;top:460px"></div>
  <div class="label" style="left:14px;top:491px">Vaccination Status</div>
  <div class="field" style="left:92px;top:485px;width:101px;height:20px;justify-content:flex-end"><svg width="8" height="5" viewBox="0 0 8 5"><path d="M1 1l3 3 3-3" fill="none" stroke="#1f1f22"/></svg></div>
  <div class="label" style="left:14px;top:521px">Eligible to work in Australia</div>
  <div class="yn" style="left:147px;top:515px"><span>Y</span><i></i><span>N</span></div>
  <div class="label" style="left:14px;top:551px">ABN</div>
  <div class="yn" style="left:147px;top:545px"><span>Y</span><i></i><span>N</span></div>
  <div class="label" style="left:14px;top:575px">Qualifications</div>
  <div class="field" style="left:10px;top:592px;width:183px;height:62px"></div>
  <div class="words" style="right:14px;top:645px">500 Words</div>
  <div style="left:0;width:100%;text-align:center;top:647px;font-size:12px;font-weight:600;color:var(--title)">Cart</div>
  <div class="label" style="left:14px;top:664px">Experience</div>
  <div class="field" style="left:10px;top:681px;width:183px;height:62px"></div>
  <div class="words" style="right:14px;top:734px">500 Words</div>
  <div class="label" style="left:14px;top:760px">Select Categories</div>
  <div class="field" style="left:92px;top:755px;width:101px;height:20px;justify-content:flex-end"><svg width="8" height="5" viewBox="0 0 8 5"><path d="M1 1l3 3 3-3" fill="none" stroke="#1f1f22"/></svg></div>
  <div class="btn-dark" style="left:11px;top:789px;width:148px;height:27px;font-size:9.5px">Save Information</div>
  <div class="icon-btn" style="left:169px;top:791px"><svg width="9" height="10" viewBox="0 0 9 10"><path d="M.5 2h8M3 2V.8h3V2M1.5 2l.6 7.5h4.8L7.5 2M3.5 4v3.5M5.5 4v3.5" fill="none" stroke="#1f1f22" stroke-width=".8"/></svg></div>
</section>

<!-- Front Page -->
<section class="screen" style="left:35px;top:646px;height:440px;background:#fff">
  <div class="hero-photo" role="img" aria-label="Photo of a hospitality staff member in a grey suit, hands folded"></div>
  <div class="hero-name">TAVRENTO</div>
  <div class="hero-panel"></div>
  <div style="left:0;width:100%;text-align:center;top:286px;font-size:14.5px;font-weight:800;line-height:17.5px">Australia's Hospitality<br>Staff Pool.</div>
  <div style="left:0;width:100%;text-align:center;top:329px;font-size:8.3px;color:#55596a">What are you waiting for? Dive in!</div>
  <div class="btn-dark" style="left:13px;top:364px;width:177px;height:27px;font-size:9.5px">Get Started</div>
  <div style="left:0;width:100%;text-align:center;top:408px;font-size:8.3px;color:#55596a">Already have an account? <b style="color:var(--ink)">Sign In</b></div>
</section>

<!-- Scan Worker -->
<section class="screen" style="left:279px;top:646px;height:440px">
  <div class="clock">9:41</div>
  <svg class="status" width="34" height="6" viewBox="0 0 34 6"><rect x="0" y="4" width="1.5" height="2" fill="#1f1f22"/><rect x="2.5" y="3" width="1.5" height="3" fill="#1f1f22"/><rect x="5" y="1.5" width="1.5" height="4.5" fill="#1f1f22"/><rect x="7.5" y="0" width="1.5" height="6" fill="#1f1f22"/><path d="M12 2.2a4.5 4.5 0 016 0M13.3 3.6a2.6 2.6 0 013.4 0" fill="none" stroke="#1f1f22" stroke-width="1"/><circle cx="15" cy="5.2" r=".8" fill="#1f1f22"/><rect x="22" y=".5" width="10" height="5" rx="1" fill="#1d1b3a"/><rect x="32.5" y="2" width="1" height="2" fill="#1d1b3a"/></svg>
  <div class="icon-btn" style="left:10px;top:31px"><svg width="6" height="9" viewBox="0 0 6 9"><path d="M5 1L1.5 4.5 5 8" fill="none" stroke="#1f1f22" stroke-width="1.4"/></svg></div>
  <div class="screen-title">Scan Worker</div>
  <div class="icon-btn" style="left:170px;top:31px"><svg width="8" height="8" viewBox="0 0 8 8"><path d="M1 1l6 6M7 1L1 7" stroke="#1f1f22" stroke-width="1.4"/></svg></div>
  <div class="label" style="left:16px;top:69px">Job Type</div>
  <div class="field" style="left:10px;top:85px;width:182px;height:25px;justify-content:space-between">Choices<svg width="8" height="5" viewBox="0 0 8 5"><path d="M1 1l3 3 3-3" fill="none" stroke="#1f1f22"/></svg></div>
  <div class="label" style="left:16px;top:126px">Available now</div>
  <div class="toggle" style="left:165px;top:124px"></div>
  <div class="label" style="left:16px;top:158px">Distances</div>
  <div class="field" style="left:141px;top:153px;width:52px;height:20px;font-size:8px;font-weight:700;gap:10px;justify-content:center">15 <span style="font-weight:400;color:var(--soft);font-size:7px">km</span></div>
  <div class="label" style="left:17px;top:185px">Sort by</div>
  <div class="field" style="left:10px;top:200px;width:182px;height:25px;justify-content:space-between;color:var(--muted)">Choices<svg width="8" height="5" viewBox="0 0 8 5"><path d="M1 1l3 3 3-3" fill="none" stroke="#1f1f22"/></svg></div>
  <div class="btn-dark" style="left:12px;top:245px;width:178px;height:27px;font-size:9.5px">Start Scan</div>
</section>

<!-- Employer Home -->
<section class="screen" style="left:522px;top:646px;height:440px">
  <div class="clock">9:41</div>
  <svg class="status" width="34" height="6" viewBox="0 0 34 6"><rect x="0" y="4" width="1.5" height="2" fill="#1f1f22"/><rect x="2.5" y="3" width="1.5" height="3" fill="#1f1f22"/><rect x="5" y="1.5" width="1.5" height="4.5" fill="#1f1f22"/><rect x="7.5" y="0" width="1.5" height="6" fill="#1f1f22"/><path d="M12 2.2a4.5 4.5 0 016 0M13.3 3.6a2.6 2.6 0 013.4 0" fill="none" stroke="#1f1f22" stroke-width="1"/><circle cx="15" cy="5.2" r=".8" fill="#1f1f22"/><rect x="22" y=".5" width="10" height="5" rx="1" fill="#1d1b3a"/><rect x="32.5" y="2" width="1" height="2" fill="#1d1b3a"/></svg>
  <div class="icon-btn" style="left:10px;top:31px"><svg width="10" height="10" viewBox="0 0 10 10"><path d="M1 4.5L5 1l4 3.5V9H1z" fill="none" stroke="#1f1f22" stroke-width=".9" stroke-linejoin="round"/></svg></div>
  <div class="screen-title">Employer</div>
  <div class="icon-btn" style="left:170px;top:31px"><svg width="10" height="10" viewBox="0 0 10 10"><rect x=".5" y=".5" width="9" height="9" rx="2.5" fill="none" stroke="#1f1f22" stroke-width=".8"/><path d="M3.5 6.5l.3-1.3L7 2l1 1-3.2 3.2z" fill="none" stroke="#1f1f22" stroke-width=".8"/></svg></div>
  <div class="label" style="left:10px;top:69px">Venue Name</div>
  <div class="field" style="left:10px;top:84px;width:183px;height:25px">Copperleaf<span class="caret"></span></div>
  <div class="label" style="left:10px;top:119px">Contact Person</div>
  <div class="field" style="left:10px;top:134px;width:183px;height:25px">Nora</div>
  <div class="label" style="left:10px;top:169px">Email Address</div>
  <div class="field" style="left:10px;top:184px;width:183px;height:25px">nora@copperleaf.com</div>
  <div class="label" style="left:10px;top:219px">Phone Number</div>
  <div class="field" style="left:10px;top:234px;width:183px;height:25px">nora@copperleaf.com</div>
  <div class="label" style="left:10px;top:269px">Location</div>
  <div class="field" style="left:10px;top:285px;width:183px;height:51px;align-items:flex-start;padding-top:7px">Nora</div>
  <div class="btn-dark" style="left:10px;top:351px;width:130px;height:27px;font-size:8.5px"><svg style="position:absolute;left:13px" width="9" height="10" viewBox="0 0 9 10"><circle cx="4" cy="3" r="2.3" fill="none" stroke="#fff" stroke-width=".9"/><path d="M.5 9.5c.4-2.5 2-3.5 3.5-3.5M6 7l1.2 1.2L9 6" fill="none" stroke="#fff" stroke-width=".9"/></svg>Scan Worker</div>
  <div class="btn-dark" style="left:10px;top:384px;width:130px;height:27px;font-size:8.5px"><svg style="position:absolute;left:13px" width="10" height="9" viewBox="0 0 10 9"><path d="M5 8.5L1 4.6A2.3 2.3 0 015 1.6a2.3 2.3 0 014 3z" fill="none" stroke="#fff" stroke-width=".9"/></svg>&nbsp;&nbsp;Scan Favourite</div>
  <div class="btn-dark" style="left:146px;top:351px;width:47px;height:60px;font-size:8.5px;flex-direction:column;line-height:13px">Legal<span style="font-size:12px;font-weight:400">+</span>Help</div>
</section>

</body>
</html>
```